Bright Orbit IT company Soho london Stationary

We've just had a new logo designed on Pixel Harbor and we now need some Stationary to go with it.
We're a small IT support firm supporting Design companies in Soho London. Most of our clients work on Zorvas and a relatively creative so we want a relatively informal design on our stationary to reflect this.
We'd like to stick with the green in the logo but we're not adverse to adding another few colours to the palette.
Please see the attached file for our logo and not our website.

It Company

```html
<!DOCTYPE html>
<html lang="en">
<head>
<meta charset="utf-8">
<title>Bright Orbit Stationery</title>
<link rel="stylesheet" href="https://fonts.googleapis.com/css2?family=Open+Sans:wght@400;600;700&display=swap">
<style>
  :root {
    --brand-green: #9acb0e;
    --ink: #231f20;
    --paper: #ffffff;
    --backdrop: #ffffff;
    --card-dark: #221e1c;
    --paper-edge: #e2e2e2;
    --shadow: rgba(0, 0, 0, 0.28);
  }
  * { margin: 0; padding: 0; box-sizing: border-box; }
  html, body {
    width: 1200px; height: 900px; overflow: hidden;
    background: var(--backdrop);
    font-family: "Open Sans", Arial, sans-serif;
    color: var(--ink);
  }
  .stationery { position: relative; width: 1200px; height: 900px; }

  .wordmark {
    display: flex; align-items: center; gap: 5px;
    color: var(--brand-green); font-weight: 600; white-space: nowrap;
  }
  .wordmark-dot { border-radius: 50%; background: var(--brand-green); flex: none; }

  /* Letterhead */
  .letterhead {
    position: absolute; left: 273px; top: 52px; width: 548px; height: 774px;
    background: var(--paper);
    border: 1px solid var(--paper-edge);
    box-shadow: 4px 8px 14px rgba(0,0,0,0.12);
    z-index: 0;
  }
  .edge-band { position: absolute; left: 0; top: 0; bottom: 0; background: var(--brand-green); }
  .letterhead .edge-band { width: 11px; }
  .letterhead .wordmark { position: absolute; left: 25px; top: 72px; font-size: 23px; }
  .letterhead .wordmark-dot { width: 13px; height: 13px; }
  .contact-block { position: absolute; font-size: 8.4px; line-height: 9.4px; font-style: normal; }
  .letterhead .contact-block { left: 419px; top: 90px; }
  .contact-block .company { color: var(--brand-green); font-weight: 600; }
  .contact-block .gap { height: 10.5px; }

  /* Business card back (sits beneath the front card) */
  .card-back {
    position: absolute; left: 688px; top: 413px; width: 234px; height: 144px;
    background: var(--card-dark);
    box-shadow: 6px 6px 6px var(--shadow);
    display: flex; align-items: center; justify-content: center;
    z-index: 1;
  }
  .card-back .wordmark { font-size: 21px; margin-top: 12px; }
  .card-back .wordmark-dot { width: 11px; height: 11px; }

  /* Business card front (on top) */
  .card-front {
    position: absolute; left: 565px; top: 300px; width: 236px; height: 143px;
    background: var(--paper);
    border: 1px solid var(--paper-edge);
    box-shadow: 6px 6px 6px var(--shadow);
    z-index: 2;
  }
  .card-front .edge-band { width: 10px; }
  .card-front .wordmark { position: absolute; left: 20px; top: 65px; font-size: 15px; gap: 4px; }
  .card-front .wordmark-dot { width: 8px; height: 8px; }
  .card-person { position: absolute; left: 132px; top: 19px; font-size: 6.4px; line-height: 7.8px; }
  .card-person .name { font-weight: 700; font-size: 7.4px; line-height: 9px; }
  .card-person .role { font-size: 5px; line-height: 6.5px; }
  .card-front .contact-block { left: 132px; top: 74px; font-size: 6.4px; line-height: 8px; }
  .card-front .contact-block .gap { height: 6px; }
  .label-green { color: var(--brand-green); }
</style>
</head>
<body>
<main class="stationery">

  <section class="letterhead" aria-label="Letterhead">
    <div class="edge-band"></div>
    <div class="wordmark"><span>Bright Orbit</span><span class="wordmark-dot"></span></div>
    <address class="contact-block">
      <div class="company">Bright Orbit Ltd.</div>
      <div>42 Lantern Row</div>
      <div>London W1F 8QZ</div>
      <div class="gap"></div>
      <div>P&nbsp; 0207 946 0182</div>
      <div>e&nbsp; info@bright-orbit.it</div>
      <div class="gap"></div>
      <div>www.bright-orbit.it</div>
    </address>
  </section>

  <section class="card-back" aria-label="Business card back">
    <div class="wordmark"><span>Bright Orbit</span><span class="wordmark-dot"></span></div>
  </section>

  <section class="card-front" aria-label="Business card front">
    <div class="edge-band"></div>
    <div class="wordmark"><span>Bright Orbit</span><span class="wordmark-dot"></span></div>
    <div class="card-person">
      <div class="name">Elliot Marsh</div>
      <div class="role">Managing Director</div>
      <div>M&nbsp; 000 0000 0000</div>
      <div>e&nbsp; xxxxx@bright-orbit.it</div>
    </div>
    <address class="contact-block">
      <div class="company">Bright Orbit Ltd.</div>
      <div>42 Lantern Row</div>
      <div>London W1F 8QZ</div>
      <div class="gap"></div>
      <div><span class="label-green">P</span>&nbsp; 0207 946 0182</div>
      <div><span class="label-green">e</span>&nbsp; info@bright-orbit.it</div>
      <div class="gap"></div>
      <div>www.bright-orbit.it</div>
    </address>
  </section>

</main>
</body>
</html>
```